varnuko.com car care product labeling with cut outs will be printed on holographic sheet.

Need to make label for eco-friendly car care products. no hazard signs.
clean and simple design minimalism
wheel cleaner
tire shiner
glass cleaner
all purpose cleaner
247x90mm
166x150mm

Target Market(s)

eco friendly car care products. europe , uae

Industry/Entity Type

car care products, eco-friendly product line

Requirements
Must have
• BW design print on holographic sheet/label .eco-friendly signs
Nice to have
• premium product look and simplicity will be at first place, can be with cut outs

```html
<!DOCTYPE html>
<html lang="en">
<head>
<meta charset="utf-8">
<title>varnuko car care labels</title>
<link rel="stylesheet" href="https://fonts.googleapis.com/css2?family=Montserrat:wght@400;500;600&display=swap">
<style>
  :root {
    --backdrop: #dcdcdc;
    --label-black: #0c0c0c;
    --holo-violet: #b77be0;
    --holo-pink: #e08fb0;
    --holo-gold: #d9c27a;
    --holo-green: #7fd98a;
    --holo-teal: #4fc7b0;
    --holo-blue: #6aa8e6;
    --brand-tone: #d890c4;
    --pill-text: #1a1a1a;
    --small-text: #c9c9c9;
    --holo: linear-gradient(90deg, var(--holo-violet), var(--holo-pink) 30%, var(--holo-gold) 55%, var(--holo-green) 75%, var(--holo-teal));
  }
  * { box-sizing: border-box; margin: 0; padding: 0; }
  html, body {
    width: 1200px; height: 800px; overflow: hidden;
    background: var(--backdrop);
    font-family: "Montserrat", sans-serif;
  }
  .label-row {
    position: relative; width: 1200px; height: 800px;
    display: flex; justify-content: center; align-items: center; gap: 46px;
  }
  .label {
    position: relative;
    width: 224px; height: 370px;
    background: var(--label-black);
    color: #fff;
    text-align: center;
  }
  .brand-name {
    position: absolute; top: 30px; left: 0; right: 0;
    font-size: 34px; font-weight: 500; letter-spacing: -0.5px;
    color: var(--brand-tone);
  }
  .car-spark-icon {
    position: absolute; top: 92px; left: 50%; transform: translateX(-50%);
    width: 42px; height: 30px; border-radius: 6px;
    background: linear-gradient(90deg, var(--holo-gold), var(--holo-violet));
    opacity: .85;
  }
  .product-title {
    position: absolute; top: 138px; left: 8px; right: 8px;
    font-size: 23px; font-weight: 500; line-height: 1.02;
    background: var(--holo);
    -webkit-background-clip: text; background-clip: text;
    color: transparent;
  }
  .product-title.two-line { top: 128px; }
  .product-icon {
    position: absolute; top: 200px; left: 50%; transform: translateX(-50%);
    width: 56px; height: 56px; border-radius: 50%;
    background: linear-gradient(135deg, var(--holo-teal), var(--holo-green));
  }
  .product-icon.wide { width: 72px; height: 42px; border-radius: 8px; top: 208px; }
  .product-icon.tall { width: 52px; height: 54px; border-radius: 10px; top: 212px; }
  .eco-badges {
    position: absolute; top: 284px; left: 0; right: 0;
    display: flex; justify-content: center; gap: 16px;
  }
  .badge {
    width: 32px; height: 32px; border-radius: 50%;
    border: 2px solid var(--holo-violet);
  }
  .badge.eco { border-color: var(--holo-gold); }
  .volume {
    position: absolute; top: 324px; left: 0; right: 0;
    font-size: 6px; color: var(--small-text);
  }
  .footer-line {
    position: absolute; left: 0; bottom: 14px; width: 224px; height: 24px;
  }
  .site-pill {
    position: absolute; bottom: 10px; left: 50%; transform: translateX(-50%);
    padding: 2px 9px; border-radius: 8px;
    font-size: 9px; font-weight: 600; letter-spacing: .3px;
    color: var(--pill-text);
    background: linear-gradient(90deg, var(--holo-pink), var(--holo-violet) 60%, var(--holo-teal));
  }
</style>
</head>
<body>
<main class="label-row">

  <section class="label">
    <div class="brand-name">varnuko</div>
    <div class="car-spark-icon" role="img" aria-label="Car with sparkles icon"></div>
    <h2 class="product-title">Whee Cleaner</h2>
    <div class="product-icon" role="img" aria-label="Alloy wheel icon"></div>
    <div class="eco-badges"><span class="badge eco"></span><span class="badge"></span></div>
    <p class="volume">500 ml</p>
    <svg class="footer-line" viewBox="0 0 224 24" aria-hidden="true">
      <defs><linearGradient id="line-a" x1="0" x2="1"><stop offset="0" stop-color="#7fd98a"/><stop offset=".5" stop-color="#e08fb0"/><stop offset="1" stop-color="#8a6ee0"/></linearGradient></defs>
      <path d="M0 6 Q112 20 224 4" fill="none" stroke="url(#line-a)" stroke-width="1.2"/>
    </svg>
    <span class="site-pill">varnuko.com</span>
  </section>

  <section class="label">
    <div class="brand-name">varnuko</div>
    <div class="car-spark-icon" role="img" aria-label="Car with sparkles icon"></div>
    <h2 class="product-title">Tire Shiner</h2>
    <div class="product-icon tall" role="img" aria-label="Tire icon"></div>
    <div class="eco-badges"><span class="badge eco"></span><span class="badge"></span></div>
    <p class="volume">500 ml</p>
    <svg class="footer-line" viewBox="0 0 224 24" aria-hidden="true">
      <defs><linearGradient id="line-b" x1="0" x2="1"><stop offset="0" stop-color="#7fd98a"/><stop offset=".5" stop-color="#e08fb0"/><stop offset="1" stop-color="#8a6ee0"/></linearGradient></defs>
      <path d="M0 6 Q112 20 224 4" fill="none" stroke="url(#line-b)" stroke-width="1.2"/>
    </svg>
    <span class="site-pill">varnuko.com</span>
  </section>

  <section class="label">
    <div class="brand-name">varnuko</div>
    <div class="car-spark-icon" role="img" aria-label="Car with sparkles icon"></div>
    <h2 class="product-title">Glass Cleaner</h2>
    <div class="product-icon wide" role="img" aria-label="Windscreen with wipers icon"></div>
    <div class="eco-badges"><span class="badge eco"></span><span class="badge"></span></div>
    <p class="volume">500 ml</p>
    <svg class="footer-line" viewBox="0 0 224 24" aria-hidden="true">
      <defs><linearGradient id="line-c" x1="0" x2="1"><stop offset="0" stop-color="#7fd98a"/><stop offset=".5" stop-color="#e08fb0"/><stop offset="1" stop-color="#8a6ee0"/></linearGradient></defs>
      <path d="M0 6 Q112 20 224 4" fill="none" stroke="url(#line-c)" stroke-width="1.2"/>
    </svg>
    <span class="site-pill">varnuko.com</span>
  </section>

  <section class="label">
    <div class="brand-name">varnuko</div>
    <div class="car-spark-icon" role="img" aria-label="Car with sparkles icon"></div>
    <h2 class="product-title two-line">All Purpose<br>Cleaner</h2>
    <div class="product-icon tall" role="img" aria-label="Car front with water drops icon"></div>
    <div class="eco-badges"><span class="badge eco"></span><span class="badge"></span></div>
    <p class="volume">500 ml</p>
    <svg class="footer-line" viewBox="0 0 224 24" aria-hidden="true">
      <defs><linearGradient id="line-d" x1="0" x2="1"><stop offset="0" stop-color="#7fd98a"/><stop offset=".5" stop-color="#e08fb0"/><stop offset="1" stop-color="#8a6ee0"/></linearGradient></defs>
      <path d="M0 6 Q112 20 224 4" fill="none" stroke="url(#line-d)" stroke-width="1.2"/>
    </svg>
    <span class="site-pill">varnuko.com</span>
  </section>

</main>
</body>
</html>
```